Flyer für Textilien mit individueller Bestickung oder Bedruckung
Wir waren mit der Designerin hochzufrieden. Alle Änderungen und Wünsche wurden schnell und sehr kompetent bearbeitet. Sind von dem Ergebnis begeistert.
Zielgruppe
Vertrieb von Logobekleidung, wie z.B. Strickwaren, Polo Shirts und T Shirts.
Zielgruppe sind Golfclubs, Proshops, Vereine, Schulen (Schulbekleidung ), Arztpraxen sowie alle Firmen und Institutionen, die Bekleidung mit individueller Bestickung oder Bedruckung benötigen.
Aufgabenstellung
Es soll ein Flyer erstellt werden, der nicht überfrachtet ist und dem Kunden schnelle und transparente Informationen liefert. Es sollen sich möglichst viele Branchen angesprochen fühlen. Auf den grünen Button mit "golf" sollte daher verzichtet werden.
Auf unserer Internetseite www.velmax.de wird deutlich, das es zwei Geschäftsfelder in unserer Firma gibt, Golfshop einerseits und Werbetextilien andererseits. Der gewünschte Flyer soll das Thema Werbetextilien abdecken. Im Datenanhang haben wir einen von uns erstellten Flyer angehängt, der lediglich als Anhaltspunkt gelten soll. Wir begrüssen es sehr wenn der Designer sich von der Vorlage löst. Unser Logo 'velmax artline' steht für das Werbetextil Geschäft und ist gleichzeitig unsere Marke, unter der wir unsere Strickwaren produzieren.
Die Sprache sollte Deutsch sein.

```html
<!DOCTYPE html>
<html lang="de">
<head>
<meta charset="utf-8">
<title>Velmax artline – Flyer Werbetextilien</title>
<link href="https://fonts.googleapis.com/css2?family=Lato:wght@400;700;900&family=Arimo:wght@700&display=swap" rel="stylesheet">
<style>
  :root{
    --green:#5aab2a;
    --green-soft:#b9d99a;
    --ink:#1d1d1b;
    --grey:#3c3c3b;
    --white:#ffffff;
    --stage:#e9e9e6;
  }
  *{box-sizing:border-box;margin:0;padding:0}
  html,body{width:1200px;height:754px;overflow:hidden;background:var(--stage)}
  body{position:relative;font-family:'Lato',sans-serif;color:var(--ink)}
  .flyer{position:absolute;width:868px;height:412px;background:var(--white);
    transform:scale(.852);transform-origin:0 0;overflow:hidden;
    box-shadow:0 2px 8px rgba(0,0,0,.18)}
  .flyer--knit{left:230px;top:18px}
  .flyer--polo{left:230px;top:385px}
  .abs{position:absolute}
  .title-band{position:absolute;background:var(--green);color:var(--white);display:flex;align-items:center}
  .flyer--knit .title-band{left:0;top:21px;width:697px;height:32px;padding-left:40px;font-weight:900;font-size:23px;letter-spacing:.3px}
  .flyer--polo .title-band{left:0;top:22px;width:690px;height:34px;padding-left:40px;font-family:'Arimo',sans-serif;font-size:26px}
  .brand{position:absolute;display:flex;flex-direction:column;align-items:center;justify-content:center;
    font-family:'Lato',sans-serif;font-weight:400;color:var(--grey);font-size:33px;line-height:1.05;text-align:center}
  .sidebar{position:absolute;background:var(--green);color:var(--white);padding:26px 12px 0 13px}
  .sidebar h3{font-size:16px;font-weight:700;margin-bottom:4px}
  .sidebar p{font-size:13.5px;line-height:1.3;margin-bottom:18px}
  .lead{font-weight:700;font-size:13.5px;line-height:1.35}
  .checks{list-style:none;font-size:14px;line-height:1.7}
  .checks li{display:flex;align-items:center;gap:5px}
  .checks svg{width:12px;height:12px;flex:none}
  .photo{position:absolute}
  .small{font-size:10.5px;line-height:1.35}
  .ref-head{color:var(--green);font-weight:700;font-size:13.5px;margin-bottom:8px}
  .price{position:absolute;left:328px;top:162px;width:86px;height:86px;border-radius:50%;
    background:var(--green-soft);text-align:center;padding-top:12px;color:var(--ink)}
  .price .from{font-size:15px;line-height:1}
  .price .amount{font-size:17px;font-weight:700;line-height:1.3}
  .price .tax{font-size:10px}
  .footer{position:absolute;left:0;top:370px;width:698px;height:42px;background:var(--green);
    color:var(--white);font-size:11px;line-height:1.4;padding:6px 0 0 20px}
  .footer b{font-weight:700}
</style>
</head>
<body>

<!-- Rückseite: Strickwaren -->
<section class="flyer flyer--knit">
  <div class="photo" role="img" aria-label="Regal mit gefalteten Strickpullovern in Gelb, Orange, Rosa, Rot, Blau und Dunkelblau"
       style="left:0;top:0;width:392px;height:178px;background:linear-gradient(90deg,#e9c24a 0%,#e7762f 22%,#e9a9b8 42%,#d93a32 58%,#3d5bb0 78%,#2b2e4a 100%)"></div>
  <div class="title-band">STRICKPULLOVER/-PULLUNDER</div>
  <div class="brand" style="left:700px;top:0;width:169px;height:125px">velmax<br>artline</div>
  <aside class="sidebar" style="left:700px;top:125px;width:169px;height:287px">
    <h3>Größen:</h3>
    <p>Herren: 48-58<br>Damen: 36-48</p>
    <h3>Bestickung</h3>
    <p>Veredelung möglich<br>Mindestmenge: 6 Stück</p>
    <h3>Preis</h3>
    <p>Gerne unterbreiten wir Ihnen ein individuelles Angebot!</p>
  </aside>
  <p class="lead abs" style="left:32px;top:196px;width:370px">Wir bieten Ihnen Merino-Strickpullover und -Pullunder für Damen und Herren in feinster Qualität - in verschiedenen klassischen und modischen Farben.</p>
  <ul class="checks abs" style="left:32px;top:282px">
    <li><svg viewBox="0 0 12 12"><path d="M1 6.5l3 3L11 2" fill="none" stroke="var(--green)" stroke-width="2"/></svg>100% australische Merinowolle</li>
    <li><svg viewBox="0 0 12 12"><path d="M1 6.5l3 3L11 2" fill="none" stroke="var(--green)" stroke-width="2"/></svg>bei 40 % maschinenwaschbar</li>
    <li><svg viewBox="0 0 12 12"><path d="M1 6.5l3 3L11 2" fill="none" stroke="var(--green)" stroke-width="2"/></svg>Total Easy Care Ausrüstung</li>
    <li><svg viewBox="0 0 12 12"><path d="M1 6.5l3 3L11 2" fill="none" stroke="var(--green)" stroke-width="2"/></svg>trocknergeeignet</li>
  </ul>
  <div class="photo" role="img" aria-label="Aufgefächerte V-Pullover in Schwarz, Blau, Grün, Pink und Apricot"
       style="left:252px;top:282px;width:172px;height:130px;background:linear-gradient(110deg,#2a2c3a 0%,#3f5aa0 35%,#9bb08a 55%,#e06f9a 75%,#f0a27e 100%)"></div>
  <div class="abs" style="left:435px;top:80px;width:245px">
    <p class="lead" style="text-align:justify">Klassische Farben während der Saison ab Lager (je nach Saisonverlauf) solange der Vorrat reicht.<br>Bei modischen Farben empfehlen wir Vororder.</p>
    <p class="small" style="margin-top:14px">Artikel 59939 velmax artline V-Pullunder Herren<br>Artikel 59940 velmax artline V-Pullover Herren<br>Artikel 81602 velmax artline V-Pullunder Damen<br>Artikel 81603 velmax artline V-Pullover Damen</p>
    <p class="ref-head" style="margin-top:32px">Referenzen</p>
    <p style="font-size:13.5px;line-height:1.35">Mit unseren Qualitäten sind wir seit nunmehr 15 Jahren in zahlreichen Pro Shops vertreten.</p>
    <p class="small" style="margin-top:4px">GC Talbach e.V., GC Erlenried, GC Mooshausen, GC Steinfeld, GC Birkensee, u.v.m.</p>
  </div>
</section>

<!-- Vorderseite: Poloshirts -->
<section class="flyer flyer--polo">
  <div class="title-band">POLOSHIRTS</div>
  <div class="brand" style="left:700px;top:0;width:168px;height:125px">velmax<br>artline</div>
  <aside class="sidebar" style="left:698px;top:125px;width:170px;height:287px">
    <h3>Größen:</h3>
    <p>Herren: S-3XL<br>Damen: XS-XXL<br>Kinder: 98-164</p>
    <h3>Bestickung</h3>
    <p>Veredelung möglich<br>Mindestmenge: 6 Stück</p>
    <h3>Stickpreis</h3>
    <p>Gerne unterbreiten wir Ihnen ein individuelles Angebot!</p>
  </aside>
  <p class="lead abs" style="left:30px;top:84px;width:370px">Wir bieten Ihnen ein großes Sortiment an kurzfristig verfügbaren POLO SHIRTS für Damen, Herren und Kinder aus Baumwolle, Mischqualität oder Funktions-Polyester an.</p>
  <ul class="checks abs" style="left:30px;top:146px">
    <li><svg viewBox="0 0 12 12"><path d="M1 6.5l3 3L11 2" fill="none" stroke="var(--green)" stroke-width="2"/></svg>sehr große Farbauswahl</li>
    <li><svg viewBox="0 0 12 12"><path d="M1 6.5l3 3L11 2" fill="none" stroke="var(--green)" stroke-width="2"/></svg>Lieferzeit: ab Lager, kurzfristig</li>
    <li><svg viewBox="0 0 12 12"><path d="M1 6.5l3 3L11 2" fill="none" stroke="var(--green)" stroke-width="2"/></svg>sehr große Farbauswahl</li>
  </ul>
  <div class="price"><div class="from">ab</div><div class="amount">€ 11,90</div><div class="tax">zzgl. MwSt.</div></div>
  <div class="photo" role="img" aria-label="Farbpalette der Poloshirts in vielen Farben von Rot über Gelb und Grün bis Blau und Schwarz"
       style="left:0;top:235px;width:434px;height:135px;background:linear-gradient(90deg,#d83a34 0%,#e9d04a 22%,#7cc24a 40%,#e48a2c 52%,#9b5fb0 65%,#3f67c0 80%,#3a3a3a 100%)"></div>
  <div class="photo" role="img" aria-label="Fröhliche Familie beim Golfspielen auf dem Grün"
       style="left:434px;top:15px;width:259px;height:355px;background:linear-gradient(180deg,#efe9e4 0%,#c9a48a 45%,#8fae5a 80%,#6f9a3c 100%)"></div>
  <footer class="footer">
    <b>Velmax Handelsvertretung</b> · Birkenweg 14 · 67059 Ludwigshafen<br>
    Tel. + 49 621 5590312 · Fax +49 621 5590313 · Mail: kontakt@velmax.de · Web: www.velmax.de
  </footer>
</section>

</body>
</html>
```